Ferris Contracting LLC Business Card Design

I am looking for a creative and unique business card design. We are a commercial construction general contractor. With the name "FERRIS" Contracting, I am hoping to see some neat designs that correlate with the name.

```html
<!DOCTYPE html>
<html lang="en">
<head>
<meta charset="utf-8">
<title>Ferris Contracting LLC – Business Card</title>
<link rel="stylesheet" href="https://fonts.googleapis.com/css2?family=Michroma&family=Raleway:wght@300;400&display=swap">
<style>
  :root {
    --stage: #3a3b3e;
    --stage-edge: #1e1f21;
    --card-dark: #050505;
    --card-mid: #1c1c1e;
    --card-light: #2e2f31;
    --brand-blue: #2f9be0;
    --text-light: #d9d9d9;
    --text-soft: #bfbfbf;
  }
  * { margin: 0; padding: 0; box-sizing: border-box; }
  html, body { width: 1200px; height: 900px; overflow: hidden; }
  body {
    background: radial-gradient(ellipse at 60% 40%, var(--stage) 0%, var(--stage-edge) 100%);
    position: relative;
    font-family: "Raleway", sans-serif;
  }
  .card {
    position: absolute;
    left: 290px;
    width: 620px;
    height: 354px;
    overflow: hidden;
    box-shadow: 0 18px 40px rgba(0,0,0,0.55);
  }
  .card--details { top: 80px; }
  .card--brand { top: 466px; }
  .card__texture {
    position: absolute; inset: 0;
    background: linear-gradient(135deg, var(--card-light) 0%, var(--card-mid) 35%, var(--card-dark) 60%, var(--card-mid) 100%);
  }
  .card--brand .card__texture {
    background: radial-gradient(ellipse at 50% 55%, var(--card-dark) 0%, var(--card-dark) 35%, var(--card-mid) 75%, var(--card-light) 100%);
  }
  .holder {
    position: absolute; left: 40px; top: 44px;
  }
  .holder__name {
    font-family: "Michroma", sans-serif;
    color: var(--brand-blue);
    font-size: 22px;
    letter-spacing: 1px;
  }
  .holder__role {
    font-weight: 300;
    color: var(--text-light);
    font-size: 20px;
    letter-spacing: 1.5px;
    margin-top: 4px;
  }
  .contacts {
    position: absolute; right: 36px; top: 150px;
    list-style: none;
    text-align: right;
  }
  .contacts__item {
    display: flex; align-items: center; justify-content: flex-end; gap: 12px;
    color: var(--text-soft);
    font-weight: 300;
    font-size: 15px;
    letter-spacing: 1.5px;
    text-transform: uppercase;
    margin-bottom: 10px;
  }
  .contacts__icon { width: 14px; height: 14px; fill: var(--brand-blue); flex: none; }
  .brand {
    position: absolute; left: 0; right: 0; top: 50%;
    transform: translateY(-50%);
    display: flex; align-items: center; justify-content: center; gap: 14px;
  }
  .brand__mark { width: 20px; height: 20px; border-radius: 50%; background: var(--brand-blue); }
  .brand__name {
    font-family: "Michroma", sans-serif;
    color: var(--brand-blue);
    font-size: 34px;
    letter-spacing: 3px;
  }
</style>
</head>
<body>
  <section class="card card--details">
    <div class="card__texture" role="img" aria-label="Glossy black woven tile pattern background"></div>
    <div class="holder">
      <p class="holder__name">MR. DALTON PRYCE</p>
      <p class="holder__role">FOUNDER</p>
    </div>
    <ul class="contacts">
      <li class="contacts__item">(251) 555-0148
        <svg class="contacts__icon" viewBox="0 0 24 24"><path d="M6.6 10.8a15 15 0 0 0 6.6 6.6l2.2-2.2a1 1 0 0 1 1-.25 11.4 11.4 0 0 0 3.6.57 1 1 0 0 1 1 1V20a1 1 0 0 1-1 1A17 17 0 0 1 3 4a1 1 0 0 1 1-1h3.5a1 1 0 0 1 1 1c0 1.25.2 2.45.57 3.57a1 1 0 0 1-.25 1z"/></svg>
      </li>
      <li class="contacts__item">info@ferrisbuilds.com
        <svg class="contacts__icon" viewBox="0 0 24 24"><path d="M2 5h20v14H2z M2 5l10 8 10-8" fill="none" stroke="#2f9be0" stroke-width="2"/></svg>
      </li>
      <li class="contacts__item">www.ferrisbuilds.com
        <svg class="contacts__icon" viewBox="0 0 24 24"><circle cx="12" cy="12" r="9" fill="none" stroke="#2f9be0" stroke-width="2"/><path d="M3 12h18M12 3c3 3 3 15 0 18M12 3c-3 3-3 15 0 18" fill="none" stroke="#2f9be0" stroke-width="1.5"/></svg>
      </li>
    </ul>
  </section>

  <section class="card card--brand">
    <div class="card__texture" role="img" aria-label="Glossy black woven tile pattern background"></div>
    <div class="brand">
      <span class="brand__mark"></span>
      <span class="brand__name">FERRIS CONTRACTING</span>
    </div>
  </section>
</body>
</html>
```